Bride Basecamp

I am looking for a design for http://www.bridebasecamp.co.uk/ its a joomla site and I am going to set up with the same mods as our stag version http://www.groomsnightout.co.uk/ you will see on groomsnight how all the menus look and are positioned. Here is an example of a activity page http://www.groomsnightout.co.uk/activity/white-water-rafting-in-perthshire.html which comes from Kiva.

The design needs to be built for responsive layout. The brand look and feel needs to be 100% for the female market.

We can accept the design in photoshop or something similar

Please ask questions if you require more information.

some examples of hen sites

http://www.girlsgetaway.co.uk/

```html
<!DOCTYPE html>
<html lang="en">
<head>
<meta charset="utf-8">
<title>Bride Basecamp</title>
<link href="https://fonts.googleapis.com/css2?family=Archivo+Black&family=Open+Sans:wght@400;600;700&family=Lato:wght@300;400&display=swap" rel="stylesheet">
<style>
  :root{
    --black:#0b0b0b;
    --ink:#1a1a1a;
    --white:#ffffff;
    --red:#e0332f;
    --deep-red:#6e1414;
    --grey-text:#8a8a8a;
    --light-line:#e4e4e4;
    --head:"Archivo Black", "Arial Black", sans-serif;
    --body:"Open Sans", Arial, sans-serif;
    --thin:"Lato", Arial, sans-serif;
  }
  *{margin:0;padding:0;box-sizing:border-box;}
  html,body{width:1200px;height:4839px;overflow:hidden;background:var(--white);}
  body{position:relative;font-family:var(--body);color:var(--ink);}
  .abs{position:absolute;}
  .photo{position:absolute;}

  /* Navigation */
  .topbar{left:0;top:0;width:1200px;height:58px;background:var(--black);z-index:5;}
  .brand{position:absolute;left:52px;top:14px;display:flex;align-items:center;gap:10px;color:var(--white);font-family:var(--head);font-size:22px;letter-spacing:1px;}
  .brand-dot{width:16px;height:16px;border-radius:50%;background:var(--red);}
  .main-nav{position:absolute;left:0;top:22px;width:1200px;}
  .main-nav a{position:absolute;color:var(--white);font-family:var(--body);font-weight:700;font-size:12px;text-decoration:none;letter-spacing:.5px;}

  /* Hero */
  .hero{left:0;top:0;width:1200px;height:620px;background:linear-gradient(100deg,#6a3a2e 0%,#c48a62 30%,#8a5a58 55%,#5a3a4a 80%,#2a1a22 100%);}
  .hero-copy{left:40px;top:272px;color:var(--white);font-family:var(--head);text-transform:uppercase;}
  .hero-kicker{font-size:38px;line-height:1.1;}
  .hero-title{font-size:50px;line-height:1.05;}
  .hero-link{font-size:34px;line-height:1.25;margin-top:6px;}
  .hero-tag{left:1112px;top:302px;width:88px;height:46px;background:var(--red);color:var(--white);font-family:var(--head);font-size:13px;line-height:1.2;padding:6px 8px;}

  /* Section headings */
  .section-title{width:1200px;left:0;text-align:center;font-family:var(--head);font-size:40px;text-transform:uppercase;}

  /* Peek grid */
  .peek-grid{left:161px;top:794px;width:887px;height:290px;display:grid;grid-template-columns:repeat(6,146px);grid-template-rows:142px 142px;column-gap:2px;row-gap:6px;}
  .peek-text{background:var(--white);border:1px solid var(--light-line);padding:14px 10px;}
  .peek-text .label{color:var(--red);font-size:9px;font-weight:700;text-transform:uppercase;}
  .peek-text h3{font-family:var(--head);font-size:14px;line-height:1.1;text-transform:uppercase;margin-top:3px;}
  .peek-text .meta{font-size:8px;color:var(--grey-text);margin-top:14px;}
  .peek-text.accent{background:var(--red);color:var(--white);border:none;}
  .peek-text.accent .label,.peek-text.accent .meta{color:var(--white);}

  /* Featured band */
  .featured{left:0;top:1194px;width:1200px;height:846px;background:linear-gradient(160deg,#3a3a34 0%,#7a7468 40%,#9a948a 60%,#4a4844 100%);clip-path:polygon(0 0,1200px 190px,1200px 846px,0 766px);}
  .featured-title{top:1520px;color:var(--white);}
  .featured-lede{left:180px;top:1614px;width:840px;text-align:center;color:var(--white);font-size:12px;font-weight:700;line-height:1.6;text-transform:uppercase;}
  .activity-grid{left:161px;top:1677px;width:880px;display:grid;grid-template-columns:repeat(6,145px);grid-auto-rows:140px;gap:2px 2px;row-gap:12px;}
  .activity{position:relative;}
  .activity .more{position:absolute;left:0;top:58px;width:100%;text-align:center;color:var(--white);font-family:var(--head);font-size:14px;}

  /* News */
  .news-title{left:20px;top:2245px;font-family:var(--head);font-size:74px;line-height:1;}
  .news-lead-photo{left:0;top:2332px;width:562px;height:450px;background:radial-gradient(ellipse at 45% 60%,#d9a98a 0%,#c7d6dc 45%,#e8f0f2 100%);}
  .news-card{position:absolute;padding:12px 12px;}
  .news-card .label{color:var(--red);font-size:9px;font-weight:700;text-transform:uppercase;}
  .news-card h3{font-family:var(--head);font-size:24px;line-height:1.02;text-transform:uppercase;}
  .news-card .date{font-size:8px;color:var(--grey-text);margin-top:10px;}
  .news-card p{font-size:9px;color:var(--grey-text);line-height:1.55;margin-top:12px;}
  .news-divider{position:absolute;background:var(--light-line);}

  /* Newsletter */
  .newsletter{left:0;top:2903px;width:1200px;height:680px;background:linear-gradient(180deg,#1e1e1e 0%,#5a5a5a 45%,#2e2e2e 100%);clip-path:polygon(0 0,1200px 195px,1200px 480px,0 680px);}
  .newsletter-title{top:3200px;color:var(--white);}
  .newsletter-text{left:230px;top:3295px;width:740px;text-align:center;color:var(--white);font-size:16px;line-height:1.5;}
  .email-field{left:565px;top:3384px;width:332px;height:44px;border:1px solid #9a9a9a;color:var(--white);font-size:11px;text-transform:uppercase;display:flex;align-items:center;justify-content:center;}

  /* Testimonials */
  .reviews-title{left:0;width:1200px;top:3735px;text-align:center;font-family:var(--thin);font-weight:400;font-size:34px;color:#333;}
  .reviews-lede{left:330px;top:3800px;width:540px;text-align:center;font-size:11px;color:var(--grey-text);line-height:1.5;}
  .review{position:absolute;width:230px;}
  .review .avatar{width:52px;height:52px;border-radius:50%;margin:0 auto;background:radial-gradient(circle,#d8b59a 0%,#b48a6a 70%);}
  .review .line{height:1px;background:var(--light-line);margin:8px 0 12px;}
  .review p{font-size:11px;color:var(--grey-text);line-height:1.5;}
  .review .mark{text-align:right;font-family:var(--head);font-size:22px;color:#cccccc;line-height:1;}

  /* Footer */
  .footer{left:0;top:4161px;width:1200px;height:678px;background:linear-gradient(180deg,#8a1e1e 0%,#5a1212 45%,#2a0808 100%);clip-path:polygon(0 0,1200px 160px,1200px 678px,0 678px);}
  .footer-head{left:161px;top:4448px;color:var(--white);font-family:var(--head);font-size:22px;line-height:1.15;text-transform:uppercase;}
  .footer-col{position:absolute;top:4532px;color:var(--white);}
  .footer-col h4{font-family:var(--head);font-size:16px;text-transform:uppercase;margin-bottom:10px;}
  .footer-col li{list-style:none;font-size:8.5px;line-height:2;text-transform:uppercase;}
  .footer-rule{left:161px;top:4768px;width:880px;height:1px;background:rgba(255,255,255,.25);}
  .copyright{left:161px;top:4778px;color:rgba(255,255,255,.7);font-size:8px;}
</style>
</head>
<body>

  <!-- Hero -->
  <div class="abs hero photo" role="img" aria-label="Group of smiling women celebrating inside a limousine"></div>

  <header class="abs topbar">
    <div class="brand"><span class="brand-dot"></span>BRIDE BASECAMP</div>
    <nav class="main-nav">
      <a style="left:348px">HOME</a>
      <a style="left:420px">LOCATIONS</a>
      <a style="left:522px">EUROPEAN DESTINATIONS</a>
      <a style="left:700px">CONTACT</a>
      <a style="left:792px">LOGIN</a>
    </nav>
  </header>

  <div class="abs hero-copy">
    <div class="hero-kicker">Sound Limo</div>
    <div class="hero-title">Girl Night Out In Style</div>
    <div class="hero-link">Read More</div>
  </div>
  <div class="abs hero-tag">NIGHT<br>SPECIAL</div>

  <!-- Peek -->
  <h2 class="abs section-title" style="top:688px">Peek This Ones Out</h2>
  <section class="abs peek-grid">
    <div class="peek-text"><div class="label">Action Men</div><h3>Play With Boys Toys</h3><div class="meta">Weekend special<br>from £49</div></div>
    <div class="photo" style="position:relative;background:linear-gradient(135deg,#1a1a1a,#5a5a5a)" role="img" aria-label="Portrait of a performer in dark studio light"></div>
    <div class="peek-text"><div class="label">Special Night</div><h3>Ride In Style In A Sound Limo</h3><div class="meta">Night special<br>from £39</div></div>
    <div class="photo" style="position:relative;background:linear-gradient(135deg,#7a3a8a,#c28ab0)" role="img" aria-label="Women posing together in a purple lit room"></div>
    <div class="peek-text"><div class="label">Shopping Frenzy</div><h3>Get The Girls And The Credit</h3><div class="meta">City break<br>from £29</div></div>
    <div class="photo" style="position:relative;background:linear-gradient(135deg,#8a6a5a,#d8c0b0)" role="img" aria-label="Four friends smiling together"></div>

    <div class="photo" style="position:relative;background:linear-gradient(135deg,#c8a890,#f0e0d4)" role="img" aria-label="Woman relaxing during a spa treatment"></div>
    <div class="peek-text"><div class="label">Mh Bese</div><h3>Be Indulged In Any Spa</h3><div class="meta">Spa day<br>from £59</div></div>
    <div class="photo" style="position:relative;background:linear-gradient(135deg,#8a1a1a,#e0603a)" role="img" aria-label="Colourful party food on a table"></div>
    <div class="peek-text accent"><div class="label">Scotland Special</div><h3>Quality Spa Days Cheap Rate</h3><div class="meta">Limited offer<br>from £45</div></div>
    <div class="photo" style="position:relative;background:linear-gradient(135deg,#1a2a6a,#3a5ab0)" role="img" aria-label="Crowd at a nightclub under blue lights"></div>
    <div class="peek-text"><div class="label">Girls Nights</div><h3>Thats Right Girls Can Take A Peek</h3><div class="meta">Evening show<br>from £35</div></div>
  </section>

  <!-- Featured activities -->
  <div class="abs featured photo" role="img" aria-label="Women laughing together outdoors under trees"></div>
  <h2 class="abs section-title featured-title">Featured Activities</h2>
  <p class="abs featured-lede">Lorem ipsum dolor sit amet, consectetur adipiscing elit. Nunc viverra blandit sagittis. Aliquam aliquam, lorem<br>ac sagittis scelerisque, eros ante porta lorem, ut posuere massa orci in turpis.</p>
  <section class="abs activity-grid">
    <div class="activity photo" style="position:relative;background:linear-gradient(135deg,#a8684a,#d89a78)" role="img" aria-label="Male dancer torso"></div>
    <div class="activity photo" style="position:relative;background:linear-gradient(180deg,#6aa8d8,#e8e0d0)" role="img" aria-label="Yacht on the sea"></div>
    <div class="activity photo" style="position:relative;background:linear-gradient(180deg,#7ac0e0,#e0c0a0)" role="img" aria-label="Women in swimwear on a beach"></div>
    <div class="activity photo" style="position:relative;background:linear-gradient(180deg,#8ac0e8,#7a5a3a)" role="img" aria-label="Quad bikes on a dirt track"></div>
    <div class="activity photo" style="position:relative;background:linear-gradient(180deg,#5a7a4a,#2a3a2a)" role="img" aria-label="Man in a suit outdoors"></div>
    <div class="activity photo" style="position:relative;background:linear-gradient(180deg,#3a2a3a,#c04a4a)" role="img" aria-label="Dancers on a stage"></div>

    <div class="activity photo" style="position:relative;background:linear-gradient(180deg,#3a6ab0,#e8e8f0)" role="img" aria-label="White houses with blue domes by the sea"></div>
    <div class="activity photo" style="position:relative;background:linear-gradient(135deg,#c88a7a,#e0a090)" role="img" aria-label="Destination highlight"><div class="more">KNOW MORE</div></div>
    <div class="activity photo" style="position:relative;background:linear-gradient(180deg,#8ab0d8,#d8c8b0)" role="img" aria-label="Classical gazebo with columns"></div>
    <div class="activity photo" style="position:relative;background:linear-gradient(180deg,#9ac0e0,#b0905a)" role="img" aria-label="Historic castle on a hill"></div>
    <div class="activity photo" style="position:relative;background:linear-gradient(180deg,#3a1a4a,#d04a6a)" role="img" aria-label="Cabaret show with dancers"></div>
    <div class="activity photo" style="position:relative;background:linear-gradient(180deg,#1a1a6a,#6a3ab0)" role="img" aria-label="Fireworks and stage lights"></div>
  </section>

  <!-- News -->
  <h2 class="abs news-title">NEWS</h2>
  <div class="abs news-lead-photo photo" role="img" aria-label="Smiling woman resting her head on a towel at a spa"></div>

  <article class="news-card" style="left:568px;top:2332px;width:200px;height:450px;">
    <div class="label">In Spotlight</div>
    <h3>Our Spas Selection Just Got Bigger</h3>
    <div class="date">November 28, 2014</div>
    <p>Lorem ipsum dolor sit amet, consectetur adipiscing elit. Nunc viverra blandit sagittis. Aliquam aliquam, lorem ac sagittis scelerisque, eros ante porta lorem.</p>
    <p>Ut posuere massa orci in turpis. Integer a facilisis nisl, sed tempus enim. Donec at varius mauris, id ornare leo.</p>
    <p>Curabitur vitae lorem sed nisi faucibus tempor. Morbi non arcu sed quam luctus porta nec sit amet elit.</p>
  </article>

  <div class="photo" style="left:768px;top:2332px;width:219px;height:150px;background:linear-gradient(135deg,#4a1a6a,#9a3ab0)" role="img" aria-label="Hen party poster with purple lights"></div>
  <article class="news-card" style="left:768px;top:2486px;width:219px;">
    <div class="label">Nightlife</div>
    <h3>London New Nightclub</h3>
    <div class="date">November 24, 2014</div>
  </article>
  <div class="photo" style="left:868px;top:2560px;width:119px;height:222px;background:linear-gradient(180deg,#e8d0b8,#b8a8a0)" role="img" aria-label="Blonde woman in a white dress"></div>

  <article class="news-card" style="left:987px;top:2332px;width:213px;height:150px;">
    <div class="label">News</div>
    <h3>1000 Happy Hens Last Monday</h3>
    <div class="date">November 20, 2014</div>
  </article>
  <div class="photo" style="left:987px;top:2484px;width:213px;height:146px;background:linear-gradient(135deg,#1a3a8a,#d05aa0)" role="img" aria-label="Colourful cocktails at a bar"></div>
  <article class="news-card" style="left:987px;top:2630px;width:213px;">
    <div class="label">About</div>
    <h3>Our Team Is Now 1 Plus</h3>
    <div class="date">November 18, 2014</div>
  </article>
  <div class="news-divider" style="left:768px;top:2482px;width:432px;height:2px;"></div>
  <div class="news-divider" style="left:767px;top:2332px;width:1px;height:450px;"></div>

  <!-- Newsletter -->
  <div class="abs newsletter photo" role="img" aria-label="Black and white concert crowd with raised hands"></div>
  <h2 class="abs section-title newsletter-title">Newsletter</h2>
  <p class="abs newsletter-text">Lorem ipsum dolor sit amet, consectetur adipiscing elit. Nunc viverra blandit sagittis. Aliquam aliquam, lorem ac sagittis scelerisque, eros ante porta lorem, ut posuere massa orci in turpis.</p>
  <div class="abs email-field">Your email address</div>

  <!-- Testimonials -->
  <h2 class="abs reviews-title">What our customer say about us</h2>
  <p class="abs reviews-lede">Lorem ipsum dolor sit amet, consectetur adipiscing elit. Nam scelerisque faucibus risus non iaculis. Fusce a augue ante, pellentesque pretium erat. Fusce in turpis in sem sed porta tristique a facilisis.</p>

  <div class="review" style="left:128px;top:3910px;">
    <div class="avatar" role="img" aria-label="Customer portrait"></div>
    <div class="line"></div>
    <p>Lorem ipsum dolor sit amet, consectetur adipiscing elit. Nam scelerisque faucibus risus non iaculis. Fusce a augue ante pellentesque.</p>
    <div class="mark">&rdquo;</div>
  </div>
  <div class="review" style="left:450px;top:3910px;">
    <div class="avatar" role="img" aria-label="Customer portrait"></div>
    <div class="line"></div>
    <p>Lorem ipsum dolor sit amet, consectetur adipiscing elit. Nam scelerisque faucibus risus non iaculis. Fusce a augue ante pellentesque.</p>
    <div class="mark">&rdquo;</div>
  </div>
  <div class="review" style="left:762px;top:3910px;">
    <div class="avatar" role="img" aria-label="Customer portrait"></div>
    <div class="line"></div>
    <p>Lorem ipsum dolor sit amet, consectetur adipiscing elit. Nam scelerisque faucibus risus non iaculis. Fusce a augue ante pellentesque.</p>
    <div class="mark">&rdquo;</div>
  </div>

  <!-- Footer -->
  <footer>
    <div class="abs footer photo" role="img" aria-label="Red tinted concert crowd with raised hands"></div>
    <div class="abs footer-head">Lorem ipsum dolor sit amet<br>consectetur adipiscing elit</div>

    <div class="footer-col" style="left:168px;">
      <h4>Locations</h4>
      <ul><li>United States</li><li>United Kingdom</li><li>Spain</li><li>France</li><li>Italy</li><li>Portugal</li><li>Greece</li><li>Others</li></ul>
    </div>
    <div class="footer-col" style="left:339px;">
      <h4>Activites</h4>
      <ul><li>Wine &amp; Treats</li><li>Spa Days</li><li>Day Packages</li><li>Bachelorette Nights</li><li>Weekend Getaways</li><li>Festivals</li><li>Sports</li><li>Other Ideas</li></ul>
    </div>
    <div class="footer-col" style="left:516px;">
      <h4>&nbsp;</h4>
      <ul><li>Lorem Ipsum</li><li>Lorem Ipsum</li><li>Lorem Ipsum</li><li>Lorem Ipsum</li><li>Lorem Ipsum</li><li>Lorem Ipsum</li><li>&nbsp;</li><li>Build Your Package</li></ul>
    </div>
    <div class="footer-col" style="left:697px;">
      <h4>Check Out</h4>
      <ul><li>Special Offers</li><li>Gift Shop</li><li>News &amp; Blog</li><li>Travel Advice</li><li>FAQs</li><li>Other Resources</li></ul>
    </div>
    <div class="footer-col" style="left:874px;">
      <h4>Basecamp</h4>
      <ul><li>About</li><li>Our Mission</li><li>Reviews</li><li>Privacy Policy</li><li>Terms &amp; Conditions</li><li>Contact</li></ul>
    </div>

    <div class="abs footer-rule"></div>
    <div class="abs copyright">All rights reserved. Copyright &copy; 2014 Bride Basecamp. All rights reserved.</div>
  </footer>

</body>
</html>
```